Executive Business Consulting for Telco Companies and Telco Start up companies

1.) Looking for an appealing and action oriented business card design.
2.)The target companies to work with start-ups and existing companies that focus on Business to Business applications
3.) For "OLRA", a Belgium based Executive consultancy company specialised in global reach starting from the centre of Europe = Brussels.
4.) Our core competence is the Go To Market in All major global regions, incl North America, Latin America, Asia, Japan, Europe and Africa.
5.) Design should be appealing to CEO, CFO and Venture Funds signalling; Expertise, Stability, Maturity and Commitment
6.) Preferred color scheme is Blue focussed and using a modern FONT.
7.) Logo design is included (uploaded)

Target Market(s)

Telecommunication Market. Companies in a B2B business model, developping services or applications to make business run more profitable

Industry/Entity Type

Business

Contact Information for Business Card

Company Name: OLRA
Name: Joris Vandekamp
Titel: Managing Director
Address: Lindelaan 58 , B-9185 Lindeveld , Belgium
Tel: + 32 471 283 915
Email: joris_vandekamp@mailbox-example.com
LinkedIn: be.profilenet-example.com/in/jorisvandekamp/

Font styles to use
Serif

Colors
0455a3
3277b5

Requirements
Must have
• Second Side Text: Operational Leadership and Reach Acceleration

```html
<!DOCTYPE html>
<html lang="en">
<head>
<meta charset="utf-8">
<title>OLRA – Business Card</title>
<link href="https://fonts.googleapis.com/css2?family=Michroma&family=Exo+2:wght@400;500&display=swap" rel="stylesheet">
<style>
  :root {
    --navy: #0b2a63;
    --blue: #0455a3;
    --blue-light: #3277b5;
    --sky: #4f95cf;
    --grey-text: #3d4a63;
    --card: #fbfbfa;
    --backdrop: #e6e7e9;
  }
  * { margin: 0; padding: 0; box-sizing: border-box; }
  html, body { width: 1200px; height: 1000px; overflow: hidden; }
  body {
    background: var(--backdrop);
    font-family: "Exo 2", sans-serif;
    position: relative;
  }
  .card {
    position: absolute;
    left: 260px;
    width: 680px;
    height: 440px;
    background: var(--card);
    box-shadow: 0 6px 18px rgba(0,0,0,0.15);
    overflow: hidden;
  }
  .card--front { top: 40px; }
  .card--back { top: 520px; }

  .brand {
    position: absolute;
    display: flex;
    align-items: center;
    font-family: "Michroma", sans-serif;
    color: var(--navy);
  }
  .brand__dot {
    border-radius: 50%;
    background: var(--blue);
    flex: none;
  }
  .card--front .brand { left: 150px; top: 70px; gap: 28px; }
  .card--front .brand__dot { width: 150px; height: 150px; }
  .card--front .brand__name { font-size: 78px; letter-spacing: 2px; }

  .tagline-band {
    position: absolute;
    left: 0; top: 262px;
    width: 640px; height: 44px;
    background: linear-gradient(90deg, var(--sky) 0%, var(--blue) 55%, var(--navy) 100%);
    display: flex; align-items: center;
    padding-left: 22px;
  }
  .tagline {
    color: #fff;
    font-size: 23px;
    letter-spacing: 0.3px;
    white-space: nowrap;
  }

  .card--back .brand { left: 30px; top: 28px; gap: 16px; }
  .card--back .brand__dot { width: 70px; height: 70px; }
  .card--back .brand__name { font-size: 38px; letter-spacing: 1px; }

  .accent-bar {
    position: absolute;
    left: 340px; top: 86px;
    width: 340px; height: 30px;
    background: linear-gradient(90deg, var(--sky) 0%, var(--blue) 50%, var(--navy) 100%);
  }
  .rule {
    position: absolute;
    left: 30px; top: 146px;
    width: 470px; height: 2px;
    background: var(--navy);
  }
  .person {
    position: absolute;
    right: 40px; top: 156px;
    text-align: right;
  }
  .person__name {
    font-family: "Michroma", sans-serif;
    font-size: 24px;
    color: var(--navy);
  }
  .person__title {
    font-size: 17px;
    color: var(--grey-text);
    margin-top: 4px;
    letter-spacing: 0.5px;
  }
  .contact-list {
    position: absolute;
    left: 30px; top: 212px;
    list-style: none;
  }
  .contact-list li {
    display: flex; align-items: center;
    gap: 12px;
    height: 40px;
    font-size: 17px;
    color: var(--grey-text);
    letter-spacing: 0.3px;
    white-space: nowrap;
  }
  .contact-icon { width: 26px; height: 26px; flex: none; }
</style>
</head>
<body>

  <section class="card card--front" aria-label="Card front">
    <div class="brand">
      <span class="brand__dot"></span>
      <span class="brand__name">OLRA</span>
    </div>
    <div class="tagline-band">
      <p class="tagline">Operational Leadership and Reach Acceleration</p>
    </div>
  </section>

  <section class="card card--back" aria-label="Card back">
    <div class="brand">
      <span class="brand__dot"></span>
      <span class="brand__name">OLRA</span>
    </div>
    <div class="accent-bar"></div>
    <div class="rule"></div>

    <div class="person">
      <p class="person__name">Joris Vandekamp</p>
      <p class="person__title">Managing Director</p>
    </div>

    <ul class="contact-list">
      <li>
        <svg class="contact-icon" viewBox="0 0 26 26" aria-hidden="true">
          <rect width="26" height="26" rx="4" fill="var(--blue-light)"/>
          <path d="M8 6c1 0 2 2 2.5 3s-1 1.5-1 2 2.5 4 4 4.5 1-1 2-1 3 1.5 3 2.5-1.5 2.5-3 2.5C11 19.5 6.5 15 6.5 9 6.5 7 7 6 8 6z" fill="#fff"/>
        </svg>
        <span>+ 32 471 283 915</span>
      </li>
      <li>
        <svg class="contact-icon" viewBox="0 0 26 26" aria-hidden="true">
          <rect width="26" height="26" rx="4" fill="var(--blue-light)"/>
          <rect x="5" y="8" width="16" height="11" fill="none" stroke="#fff" stroke-width="1.6"/>
          <path d="M5 8l8 6 8-6" fill="none" stroke="#fff" stroke-width="1.6"/>
        </svg>
        <span>joris_vandekamp@mailbox-example.com</span>
      </li>
      <li>
        <svg class="contact-icon" viewBox="0 0 26 26" aria-hidden="true">
          <rect width="26" height="26" rx="4" fill="var(--blue-light)"/>
          <path d="M13 5a5 5 0 0 1 5 5c0 4-5 10-5 10s-5-6-5-10a5 5 0 0 1 5-5z" fill="#fff"/>
          <circle cx="13" cy="10" r="2" fill="var(--blue-light)"/>
        </svg>
        <span>Lindelaan 58 , B-9185 Lindeveld , Belgium</span>
      </li>
      <li>
        <svg class="contact-icon" viewBox="0 0 26 26" aria-hidden="true">
          <rect width="26" height="26" rx="4" fill="var(--blue-light)"/>
        </svg>
        <span>be.profilenet-example.com/in/jorisvandekamp/</span>
      </li>
    </ul>
  </section>

</body>
</html>
```